The billboard should communicate confidence, energy and approachability while maintaining a professional, premium feel. Rather than relying on a standard agent photograph, property collage or crowded list of services, we would like an original creative idea that makes people look twice. This could involve a fun visual, clever headline, striking colour contrast or an unexpected real estate theme. The concept should feel positive and contemporary, with enough personality to become recognisable throughout the local community.

The key message should appeal to homeowners who are thinking about selling, preparing to sell or simply curious about the value of their property. Copy must be short, clear and conversational, supported by a direct call to action. The agent’s name, phone number and company branding should remain highly visible without competing with the main idea.

The finished billboard will measure 8.0 metres wide by 2.08 metres high (1224px x 324px), so the composition must suit a long landscape format. All important text and imagery should remain comfortably within safe margins and be legible from a distance. The design should avoid small writing, unnecessary detail and visual clutter.

The goal is to create a billboard that feels different from every other real estate sign in the area—something engaging, confident and easy to remember. It should build strong brand awareness, generate conversations and encourage local property owners to contact the agent when they are ready to make their next move. The concept should be adaptable for future campaigns, helping establish a consistent, distinctive and trusted local brand presence.

Target Market(s)

ages 30+

Industry/Entity Type

Real Estate

Requirements
Must have
• call Wade and phone number 0417 63 28 05
Nice to have
• Nice bright and yellow.. Exciting and grabbing

```html
<!DOCTYPE html>
<html lang="en">
<head>
<meta charset="utf-8">
<title>Call Wade – Billboard</title>
<link rel="stylesheet" href="https://fonts.googleapis.com/css2?family=Bebas+Neue&family=Kaushan+Script&display=swap">
<style>
  :root {
    --backdrop: #333333;
    --brand-yellow: #ffe514;
    --ink: #111111;
    --tag-white: #f7f7f5;
    --tag-shade: #e4e4e0;
    --band-black: #0c0c0c;
    --white: #ffffff;
  }
  * { margin: 0; padding: 0; box-sizing: border-box; }
  html, body {
    width: 1200px;
    height: 1001px;
    overflow: hidden;
    background: var(--backdrop);
  }
  .billboard {
    position: absolute;
    left: 126px;
    top: 377px;
    width: 948px;
    height: 246px;
    background: var(--brand-yellow);
    overflow: hidden;
  }
  .price-tag {
    position: absolute;
    left: 58px;
    top: 14px;
    width: 320px;
    height: 172px;
    transform: rotate(12deg);
    transform-origin: center;
  }
  .price-tag__back {
    position: absolute;
    left: 8px;
    top: 14px;
    width: 320px;
    height: 172px;
    border-radius: 14px;
    background: var(--tag-shade);
  }
  .price-tag__card {
    position: absolute;
    inset: 0;
    border-radius: 14px;
    background: var(--tag-white);
  }
  .headline {
    position: absolute;
    left: 150px;
    top: 10px;
    transform: rotate(12deg);
    transform-origin: left top;
    font-family: "Bebas Neue", sans-serif;
    font-weight: 400;
    font-size: 62px;
    line-height: 50px;
    color: var(--ink);
    letter-spacing: 1px;
    white-space: nowrap;
  }
  .cta-band {
    position: absolute;
    left: 234px;
    top: 196px;
    width: 192px;
    height: 40px;
    background: var(--band-black);
    transform: rotate(-2deg);
    display: flex;
    align-items: center;
    justify-content: center;
    font-family: "Bebas Neue", sans-serif;
    font-size: 30px;
    color: var(--white);
    letter-spacing: 0.5px;
    white-space: nowrap;
  }
  .agent {
    position: absolute;
    left: 486px;
    top: 18px;
    width: 380px;
    text-align: center;
  }
  .agent__call {
    font-family: "Kaushan Script", cursive;
    font-size: 64px;
    line-height: 76px;
    color: var(--ink);
    white-space: nowrap;
  }
  .agent__swoosh {
    position: absolute;
    left: 52px;
    top: 70px;
  }
  .agent__phone {
    font-family: "Bebas Neue", sans-serif;
    font-size: 74px;
    line-height: 74px;
    color: var(--ink);
    letter-spacing: 1px;
    margin-top: 10px;
    white-space: nowrap;
  }
  .rule {
    position: absolute;
    left: 486px;
    top: 187px;
    width: 379px;
    height: 1px;
    background: var(--ink);
  }
  .brand-row {
    position: absolute;
    left: 485px;
    top: 204px;
    width: 380px;
    height: 34px;
    display: flex;
    align-items: center;
    white-space: nowrap;
  }
  .brand-name {
    font-family: "Bebas Neue", sans-serif;
    font-size: 32px;
    color: var(--ink);
    letter-spacing: 0.5px;
    width: 162px;
    flex: none;
  }
  .brand-divider {
    width: 1px;
    height: 32px;
    background: var(--ink);
    margin: 0 12px 0 6px;
    flex: none;
  }
  .brand-tagline {
    font-family: "Kaushan Script", cursive;
    font-size: 15px;
    line-height: 20px;
    color: var(--ink);
    white-space: nowrap;
    flex: none;
  }
</style>
</head>
<body>
  <section class="billboard">
    <div class="price-tag" role="img" aria-label="White cardboard price tag on a string">
      <div class="price-tag__back"></div>
      <div class="price-tag__card"></div>
    </div>
    <h1 class="headline">What's<br>Your Home<br>Worth?</h1>
    <div class="cta-band">Let's find out</div>

    <div class="agent">
      <p class="agent__call">Call Wade</p>
      <svg class="agent__swoosh" width="270" height="14" viewBox="0 0 270 14" aria-hidden="true">
        <path d="M2 12 C 80 4, 190 2, 268 8 C 190 6, 90 8, 2 12 Z" fill="#111111"/>
      </svg>
      <p class="agent__phone">0417 63 28 05</p>
    </div>

    <div class="rule"></div>

    <div class="brand-row">
      <span class="brand-name">Lorne Bexley</span>
      <span class="brand-divider"></span>
      <span class="brand-tagline">You property. Our priority</span>
    </div>
  </section>
</body>
</html>
```